Electronic Time-sheet & Training Tracker for Mobile phone

App should have two functions:Access by Pelkin and Varnoth:Employee Tracker: I need to be able to add/edit employees and personal information (example: address, DL number, SS number, DOB, employee number), drug screen information (type DCCHA and expiration date, DCCFO and expiration date, DCCHT and expiration date, KOVE Background and expiration date) and enter multiple training records (BREM7 and expiration date). It would be great to receive an expiration alert.The employee would only have visibility to his own. Supervisors would have overall visibility.Time-Sheet:I need a time-sheet that can be accessed on the phone, be completed, then have the ability to electronically sign and submitted. The timesheet needs to be used two-fold for supervision to verify hours and edit (if need be), he would approve and forward to payroll. The time-sheet should be daily or weekly if we can get the data to fit. We are trying to streamline field supervisors having to log on to a computer to access a server just to do time-sheets. We need it to be user-friendly. We need to have two places to have electronic signatures (employee and supervisor).
Updates
A couple of designers have asked for an additional day. Others are making changes based on feedback.
Target Market(s)
Industrial (Oil ad Gas)
Requirements
Must have
- Timesheet portion may require multiple entries with billable, non-billable, shop drop-down and job number and category code (LRS, HTS, FMS, ITP, OBS, HTT, NDE)
Nice to have
- Tracker - Training expiration alert or notifications by email to employee and supervisors.

```html
<!DOCTYPE html>
<html lang="en">
<head>
<meta charset="utf-8">
<title>Tarvex – Time-sheet &amp; Training Tracker</title>
<link href="https://fonts.googleapis.com/css2?family=Montserrat:wght@500&family=Comfortaa:wght@500;700&display=swap" rel="stylesheet">
<style>
  :root {
    --ink: #1c1f26;
    --orange: #e06a36;
    --orange-soft: #f2a27c;
    --grey: #9a9ea6;
    --rule: #e6e7ea;
    --card: #ffffff;
    --canvas: #f3f4f6;
    --ok: #3bc45c;
    --alert: #e43b3b;
  }
  * { box-sizing: border-box; margin: 0; padding: 0; }
  html, body { width: 850px; height: 1200px; overflow: hidden; }
  body { background: var(--canvas); font-family: "Comfortaa", sans-serif; color: var(--ink); position: relative; }

  .screen { position: absolute; width: 240px; height: 520px; background: #fff; border-radius: 30px; overflow: hidden; box-shadow: 0 6px 22px rgba(28,31,38,.08); }
  .screen--login { left: 90px; top: 40px; }
  .screen--records { left: 525px; top: 40px; }
  .screen--timesheet { left: 90px; top: 664px; }
  .screen--profile { left: 525px; top: 664px; }

  /* brand: plain name in the text font, one colour, one weight */
  .brand { position: absolute; left: 0; right: 0; text-align: center; font-family: "Comfortaa", sans-serif; font-weight: 700; color: var(--ink); line-height: 1; letter-spacing: .5px; }
  .screen--login .brand { top: 90px; font-size: 24px; }

  .app-bar { position: absolute; left: 0; right: 0; top: 32px; height: 22px; }
  .app-bar .brand { top: 5px; font-size: 11px; }
  .app-bar__icon { position: absolute; top: 4px; width: 14px; height: 14px; }
  .app-bar__icon--left { left: 16px; }
  .app-bar__icon--right { right: 16px; }

  /* login */
  .login-shape { position: absolute; inset: 0; }
  .field-line { position: absolute; left: 75px; right: 9px; color: #fff; font-size: 6.5px; font-weight: 700; }
  .field-line::after { content: ""; position: absolute; left: 0; right: 0; top: 32px; border-bottom: 1px solid #5a5e68; }
  .field-line--user { top: 223px; }
  .field-line--pass { top: 268px; }
  .btn { position: absolute; background: var(--orange); color: #fff; font-size: 6px; font-weight: 700; border-radius: 9px; display: flex; align-items: center; justify-content: center; }
  .btn--login { left: 160px; top: 311px; width: 70px; height: 17px; }
  .signup { position: absolute; left: 14px; top: 500px; font-size: 6px; font-weight: 700; color: var(--ink); }
  .signup a { color: var(--orange); text-decoration: none; }

  /* records */
  .record { position: absolute; left: 10px; width: 220px; height: 37px; background: var(--card); border-radius: 3px; box-shadow: 0 1px 6px rgba(28,31,38,.07); font-size: 5.5px; font-weight: 700; }
  .record__dot { position: absolute; left: 5px; top: 6px; width: 6px; height: 6px; border-radius: 50%; background: var(--ok); }
  .record__dot--expired { background: var(--alert); }
  .record__title { position: absolute; left: 16px; top: 6px; width: 140px; line-height: 7.5px; }
  .record__code { display: block; color: var(--orange-soft); font-weight: 500; margin-top: 3px; }
  .record__code--tight { margin-top: 1px; }
  .record__dates { position: absolute; right: 8px; top: 6px; width: 62px; line-height: 7.5px; }
  .record__exp { display: block; color: var(--orange-soft); font-weight: 500; margin-top: 3.5px; }

  /* timesheet */
  .form-card { position: absolute; left: 10px; right: 10px; top: 75px; bottom: 0; background: var(--card); box-shadow: 0 0 8px rgba(28,31,38,.06); }
  .form-field { position: absolute; left: 0; right: 0; height: 42.5px; border-bottom: 1px solid var(--rule); }
  .form-field__label { position: absolute; left: 16px; top: 12px; font-size: 7px; color: var(--grey); font-weight: 500; }
  .form-field__value { position: absolute; left: 16px; top: 26px; font-family: "Montserrat", sans-serif; font-size: 9.5px; font-weight: 500; }
  .form-field--select { border-bottom: 1.5px solid var(--ink); }
  .form-field__caret { position: absolute; right: 6px; top: 28px; }
  .btn--save { left: 85px; top: 478px; width: 70px; height: 18px; }

  /* profile */
  .avatar { position: absolute; left: 83px; top: 75px; width: 74px; height: 74px; border-radius: 50%; background: radial-gradient(circle at 50% 45%, #9fd3dc, #4aa2b5 70%, #3a8798); }
  .profile-card { position: absolute; left: 10px; right: 10px; top: 180px; bottom: 0; background: var(--card); box-shadow: 0 0 8px rgba(28,31,38,.06); }
  .profile-field { position: absolute; left: 13px; }
  .profile-field__label { font-size: 5.5px; color: var(--grey); font-weight: 700; }
  .profile-field__value { font-family: "Montserrat", sans-serif; font-size: 10px; font-weight: 500; margin-top: 7px; display: flex; align-items: center; gap: 10px; }
</style>
</head>
<body>

<!-- Login -->
<section class="screen screen--login">
  <svg class="login-shape" viewBox="0 0 240 520" aria-hidden="true">
    <polygon points="240,102 0,224 240,520" fill="var(--ink)"/>
  </svg>
  <div class="brand">TARVEX</div>
  <div class="field-line field-line--user">User name</div>
  <div class="field-line field-line--pass">Password</div>
  <div class="btn btn--login">Login</div>
  <p class="signup">Create a new account? <a href="#">Sign up</a></p>
</section>

<!-- Training records -->
<section class="screen screen--records">
  <header class="app-bar">
    <svg class="app-bar__icon app-bar__icon--left" viewBox="0 0 14 14"><path d="M13 7H2M6.5 2.5 2 7l4.5 4.5" fill="none" stroke="var(--ink)" stroke-width="1.5"/></svg>
    <div class="brand">TARVEX</div>
    <svg class="app-bar__icon app-bar__icon--right" viewBox="0 0 14 14"><circle cx="5.5" cy="5.5" r="3.8" fill="none" stroke="var(--ink)" stroke-width="1.8"/><path d="M8.3 8.3 12.5 12.5" stroke="var(--ink)" stroke-width="2.4" stroke-linecap="round"/></svg>
  </header>

  <article class="record" style="top:73px"><span class="record__dot"></span><div class="record__title">Aerion Gas GMP &amp; Food Safety<span class="record__code">12ALGMP</span></div><div class="record__dates">04-23-2018<span class="record__exp">04-30-2019 (Exp.)</span></div></article>
  <article class="record" style="top:121.5px"><span class="record__dot"></span><div class="record__title">Aerion Gas MRPL Site Orientations<span class="record__code">12108AIR</span></div><div class="record__dates">04-23-2018<span class="record__exp">04-30-2019 (Exp.)</span></div></article>
  <article class="record" style="top:170px"><span class="record__dot"></span><div class="record__title">Delmar Fuels Site Orientations<br>- Brantley Flats La.<span class="record__code record__code--tight">12108AIR</span></div><div class="record__dates">04-23-2018<span class="record__exp">04-30-2019 (Exp.)</span></div></article>
  <article class="record" style="top:218.5px"><span class="record__dot"></span><div class="record__title">Aerion Gas MRPL Site Orientations<span class="record__code">12108AIR</span></div><div class="record__dates">04-23-2018<span class="record__exp">04-30-2019 (Exp.)</span></div></article>
  <article class="record" style="top:267px"><span class="record__dot record__dot--expired"></span><div class="record__title">Delmar Fuels Site Orientations<br>- Brantley Flats La.<span class="record__code record__code--tight">12108AIR</span></div><div class="record__dates">04-23-2017<span class="record__exp">04-30-2019 (Exp.)</span></div></article>
  <article class="record" style="top:315.5px"><span class="record__dot"></span><div class="record__title">Aerion Gas MRPL Site Orientations<span class="record__code">12108AIR</span></div><div class="record__dates">04-23-2018<span class="record__exp">04-30-2019 (Exp.)</span></div></article>
  <article class="record" style="top:364px"><span class="record__dot record__dot--expired"></span><div class="record__title">Delmar Fuels Site Orientations<br>- Brantley Flats La.<span class="record__code record__code--tight">12108AIR</span></div><div class="record__dates">04-23-2017<span class="record__exp">04-30-2018 (Exp.)</span></div></article>
  <article class="record" style="top:412.5px"><span class="record__dot"></span><div class="record__title">Aerion Gas MRPL Site Orientations<span class="record__code">12108AIR</span></div><div class="record__dates">04-23-2018<span class="record__exp">04-30-2019 (Exp.)</span></div></article>
</section>

<!-- Time-sheet entry -->
<section class="screen screen--timesheet">
  <header class="app-bar">
    <svg class="app-bar__icon app-bar__icon--left" viewBox="0 0 14 14"><path d="M1 3h12M1 7h12M1 11h12" stroke="var(--ink)" stroke-width="1.6"/></svg>
    <div class="brand">TARVEX</div>
    <svg class="app-bar__icon app-bar__icon--right" viewBox="0 0 14 14"><circle cx="5.5" cy="5.5" r="3.8" fill="none" stroke="var(--ink)" stroke-width="1.8"/><path d="M8.3 8.3 12.5 12.5" stroke="var(--ink)" stroke-width="2.4" stroke-linecap="round"/></svg>
  </header>
  <div class="form-card">
    <div class="form-field" style="top:0"><span class="form-field__label">Job number</span></div>
    <div class="form-field" style="top:42.5px"><span class="form-field__label">Job number</span></div>
    <div class="form-field" style="top:85px"><span class="form-field__label">Job number</span></div>
    <div class="form-field" style="top:127.5px"><span class="form-field__label">Job number</span></div>
    <div class="form-field" style="top:170px"><span class="form-field__label">Job number</span></div>
    <div class="form-field form-field--select" style="top:212.5px">
      <span class="form-field__label">Job number</span>
      <span class="form-field__value">LRS</span>
      <svg class="form-field__caret" width="8" height="7" viewBox="0 0 8 7"><path d="M0 0h8L4 7z" fill="var(--ink)"/></svg>
    </div>
  </div>
  <div class="btn btn--save">Save</div>
</section>

<!-- Profile -->
<section class="screen screen--profile">
  <header class="app-bar">
    <svg class="app-bar__icon app-bar__icon--left" viewBox="0 0 14 14"><path d="M13 7H2M6.5 2.5 2 7l4.5 4.5" fill="none" stroke="var(--ink)" stroke-width="1.5"/></svg>
    <div class="brand">TARVEX</div>
    <svg class="app-bar__icon app-bar__icon--right" viewBox="0 0 14 14"><circle cx="5.5" cy="5.5" r="3.8" fill="none" stroke="var(--ink)" stroke-width="1.8"/><path d="M8.3 8.3 12.5 12.5" stroke="var(--ink)" stroke-width="2.4" stroke-linecap="round"/></svg>
  </header>
  <div class="avatar" role="img" aria-label="Employee profile photo"></div>
  <div class="profile-card">
    <div class="profile-field" style="top:25px"><div class="profile-field__label">Full name</div><div class="profile-field__value">Nadia Holloway <svg width="9" height="9" viewBox="0 0 9 9"><path d="M1 8l1-3 5-5 2 2-5 5z" fill="var(--orange-soft)"/></svg></div></div>
    <div class="profile-field" style="top:86px"><div class="profile-field__label">Full name</div><div class="profile-field__value">United States <svg width="9" height="9" viewBox="0 0 9 9"><path d="M1 8l1-3 5-5 2 2-5 5z" fill="var(--orange-soft)"/></svg></div></div>
    <div class="profile-field" style="top:142px"><div class="profile-field__label">Full name</div><div class="profile-field__value">(555) 014 2286 <svg width="9" height="9" viewBox="0 0 9 9"><path d="M1 8l1-3 5-5 2 2-5 5z" fill="var(--orange-soft)"/></svg></div></div>
    <div class="profile-field" style="top:198px"><div class="profile-field__label">Full name</div><div class="profile-field__value">26/06/1991 <svg width="9" height="9" viewBox="0 0 9 9"><path d="M1 8l1-3 5-5 2 2-5 5z" fill="var(--orange-soft)"/></svg></div></div>
    <div class="profile-field" style="top:254px"><div class="profile-field__label">Full name</div><div class="profile-field__value">lena-91@example.com <svg width="9" height="9" viewBox="0 0 9 9"><path d="M1 8l1-3 5-5 2 2-5 5z" fill="var(--orange-soft)"/></svg></div></div>
  </div>
</section>

</body>
</html>
```